lighting products eshop web site

We need a brand new ecommerce website (only psd files for the layout) , that will sell professional lighting products in Greek territory.
Please check the sister site www.lampiroxa.gr to get an idea of the products, they will be similar, actually like the products under the menu category "ΕΠΑΓΓΕΛΜΑΤΙΚΑ".
We would like the same philosophy as far as concern the menu structure, namely the menu categories/subcategories shall be actually the products
categories/subcategories, however the menu items shall be presented in a different, more sophisticated way. As far as concern the website layout, we need a minimal, elegant
and contemporary approach that will highlight the products in a perfect manner. We prefer the white color as the main website (background) color and discrete use of brand logo colors.
That is the main idea, awaiting your personal proposal according to the aforementioned requirements
Technically speaking we use bootstrap framework in terms of design meaning 12cols with max width 1170px.
The website will be a joomla - virtuemart website

For images please use some from lampiroxa.gr
For text use any text - just to show me the space.

Industry/Entity Type

It Professional

Number of Pages Required

3 page

Font styles to use
Sans Serif

Colors
00a990
ec1f27

Requirements
Must have
• I need 4 psd pages for the website
• 1. Start page
• 2. Category page
• 3. Product details page
• 4. blog page
Nice to have
• leave designer to choose the best

```html
<!DOCTYPE html>
<html lang="en">
<head>
<meta charset="utf-8">
<title>Lumo Lumo – Blogs</title>
<link href="https://fonts.googleapis.com/css2?family=Roboto:wght@300;400;500&display=swap" rel="stylesheet">
<style>
:root{
  --green:#00a990;
  --red:#ec1f27;
  --ink:#222;
  --muted:#777;
  --line:#e6e6e6;
  --nav:#2b2b2b;
  --footer:#2d2d2d;
  --footer-bottom:#262626;
  --white:#fff;
}
*{margin:0;padding:0;box-sizing:border-box}
html,body{width:849px;height:1200px;overflow:hidden}
body{position:relative;background:var(--white);font-family:'Roboto',sans-serif;color:var(--ink);font-size:8px}
.abs{position:absolute}
a{color:inherit;text-decoration:none}

/* top bar */
.topbar{left:0;top:0;width:849px;height:28px;border-bottom:1px solid #eee}
.topbar .welcome{left:63px;top:9px;font-size:8px}
.topbar .welcome .acc{color:var(--green)}
.topbar .links{right:63px;top:9px;font-size:8px;display:flex;gap:20px}

/* header */
.header{left:0;top:28px;width:849px;height:44px}
.logo{left:63px;top:12px;font-size:20px;font-weight:300;letter-spacing:3px;color:var(--red)}
.header .tools{right:63px;top:16px;display:flex;gap:18px;font-size:8.5px;color:#444;align-items:center}
.cart-badge{display:inline-block;width:12px;height:12px;border-radius:50%;background:var(--red);color:#fff;font-size:7px;text-align:center;line-height:12px;margin-right:6px}

/* nav */
.nav{left:0;top:72px;width:849px;height:34px;background:var(--nav)}
.nav ul{position:absolute;left:63px;top:11px;display:flex;gap:19px;list-style:none;color:#fff;font-size:8.5px}
.nav ul li::after{content:" ▾";font-size:6px}
.search{left:654px;top:0;width:132px;height:34px;border-left:1px solid #444;border-right:1px solid #444;color:#aaa;font-size:7.5px;padding:11px 9px}
.search svg{position:absolute;right:10px;top:11px}

/* page title */
.pagehead{left:0;top:106px;width:849px;height:44px;border-bottom:1px solid #eee}
.pagehead h1{position:absolute;left:63px;top:15px;font-size:12px;font-weight:400;color:#555}
.crumbs{position:absolute;right:63px;top:18px;font-size:7.5px;color:#333}
.crumbs span{color:var(--muted)}

/* timeline */
.tl-icon{left:410px;top:174px}
.tl-date{left:385px;top:210px;width:80px;height:22px;background:#f3f3f3;border:1px solid #e2e2e2;font-size:7.5px;text-align:center;line-height:21px}
.tl-line{left:424px;top:232px;width:1px;height:700px;background:#ddd}
.tl-dot{width:6px;height:6px;border-radius:50%;background:#e5e5e5;left:421px}

/* cards */
.card{width:250px;height:347px;background:#fff;box-shadow:0 0 3px rgba(0,0,0,.18)}
.card .photo{width:250px;height:166px}
.card h2{position:absolute;left:16px;top:184px;font-size:12.5px;font-weight:400}
.card .meta{position:absolute;left:16px;top:205px;font-size:7px;color:var(--ink)}
.card .meta i{font-style:normal;color:var(--muted)}
.card .rule{position:absolute;left:16px;top:229px;width:218px;height:2px;border-top:1px solid var(--line);border-bottom:1px solid var(--line)}
.card p{position:absolute;left:16px;top:248px;width:218px;font-size:8px;line-height:14px;color:#555;text-align:justify}
.card .more{position:absolute;left:16px;top:318px;font-size:6.5px;font-weight:500}
.card .count{position:absolute;right:16px;top:318px;font-size:6.5px}
.pointer{width:0;height:0;border-top:3px solid transparent;border-bottom:3px solid transparent}
.card.left .pointer{position:absolute;right:-4px;top:54px;border-left:3px solid #222}
.card.right .pointer{position:absolute;left:-4px;top:108px;border-right:3px solid #222}

/* pagination */
.pager{left:0;top:960px;width:849px;display:flex;justify-content:center;align-items:center;gap:0;font-size:7px}
.pager span{display:inline-block;width:26.5px;text-align:center;line-height:18px}
.pager .cur{width:22px;height:18px;border-radius:9px;background:var(--red);color:#fff;margin:0 2px}
.pager .wide{width:44px}

/* footer */
.footer{left:0;top:998px;width:849px;height:172px;background:var(--footer);color:#fff}
.fcol{position:absolute;top:30px}
.fcol h3{font-size:12px;font-weight:500;padding-bottom:6px;position:relative}
.fcol h3::after{content:"";position:absolute;left:0;bottom:0;width:14px;height:1px;background:#fff}
.fcol ul{list-style:none;margin-top:10px;font-size:8px;line-height:19.4px}
.fcol p{margin-top:10px;font-size:8px;line-height:14px}
.social{display:flex;gap:4px;margin-top:14px}
.social span{width:26px;height:26px;background:#3a3a3a}
.email{margin-top:10px;width:178px;height:25px;background:#3a3a3a;color:#bbb;font-size:8px;padding:8px 12px}
.subscribe{margin-top:8px;width:59px;height:25px;background:var(--red);font-size:8px;text-align:center;line-height:25px}
.to-top{left:804px;top:1153px;width:28px;height:28px;border-radius:50%;background:var(--green)}
.fbottom{left:0;top:1170px;width:849px;height:30px;background:var(--footer-bottom);color:#fff;font-size:8.5px}
.fbottom .copy{position:absolute;left:63px;top:10px}
.fbottom .legal{position:absolute;right:63px;top:10px}
</style>
</head>
<body>

<div class="abs topbar">
  <div class="abs welcome">Welcome to Lumo Lumo &nbsp; <span class="acc">🔒Login</span> &nbsp; OR &nbsp; <span class="acc">↗ Signup</span></div>
  <div class="abs links"><span>My Account</span><span>Orders</span><span>Shopping Basket</span></div>
</div>

<div class="abs header">
  <div class="abs logo">LUMO LUMO</div>
  <div class="abs tools">
    <span>♡ Wish List Products</span>
    <span>Compare Products</span>
    <span>EN ▾</span>
    <span><span class="cart-badge">0</span>0,00 €</span>
  </div>
</div>

<nav class="abs nav">
  <ul><li>Hanging</li><li>Roof</li><li>Wall</li><li>Floor</li><li>Spot</li><li>Outdoor</li><li>Fans</li><li>Professional</li><li>Companies</li></ul>
  <div class="abs search">Search products here
    <svg width="11" height="11" viewBox="0 0 11 11" fill="none" stroke="#ccc" stroke-width="1.2"><circle cx="4.5" cy="4.5" r="3.6"/><path d="M7.2 7.2 10 10"/></svg>
  </div>
</nav>

<header class="abs pagehead">
  <h1>Blogs</h1>
  <div class="crumbs">HOME &nbsp; › &nbsp; <span>BLOGS</span></div>
</header>

<svg class="abs tl-icon" width="30" height="26" viewBox="0 0 30 26" fill="none" stroke="#333" stroke-width="1.2">
  <path d="M10 3h17v11h-4l-3 3v-3h-10z"/><path d="M8 9H3v11h3v4l4-4h10v-3"/>
  <circle cx="16" cy="8.5" r=".6" fill="#333"/><circle cx="18.5" cy="8.5" r=".6" fill="#333"/><circle cx="21" cy="8.5" r=".6" fill="#333"/>
</svg>
<div class="abs tl-date">19th September</div>
<div class="abs tl-line"></div>
<div class="abs tl-dot" style="top:270px"></div>
<div class="abs tl-dot" style="top:325px"></div>
<div class="abs tl-dot" style="top:634px"></div>
<div class="abs tl-dot" style="top:689px"></div>

<article class="abs card left" style="left:102px;top:218px">
  <div class="photo" role="img" aria-label="Hotel bed with white linen and olive runner" style="background:linear-gradient(160deg,#8a8378,#e9e6df 45%,#c9c2b2)"></div>
  <div class="pointer"></div>
  <h2>Blog heading here</h2>
  <div class="meta"><i>By:</i> Admin &nbsp;&nbsp; <i>Date:</i> September 19th, 2016 &nbsp;&nbsp; <i>Tags:</i> Tag1, Tag2</div>
  <div class="rule"></div>
  <p>Aenean vulputate eleifend tellus aenean leo ligula porttitor eu consequat vitae eleifend ac enim aliquam lorem ante dapibus in viverra quis feugiat a tellus phasellus viverra nulla ut metus varius laoreet quisque rutrum.</p>
  <div class="more">READ MORE →</div><div class="count">💬 2</div>
</article>

<article class="abs card right" style="left:498px;top:218px">
  <div class="photo" role="img" aria-label="Bedroom with warm bedside lamps" style="background:linear-gradient(160deg,#c47a2a,#4a3424 45%,#d8d4cf)"></div>
  <div class="pointer"></div>
  <h2>Blog heading here</h2>
  <div class="meta"><i>By:</i> Admin &nbsp;&nbsp; <i>Date:</i> September 19th, 2016 &nbsp;&nbsp; <i>Tags:</i> Tag1, Tag2</div>
  <div class="rule"></div>
  <p>Aenean vulputate eleifend tellus aenean leo ligula porttitor eu consequat vitae eleifend ac enim aliquam lorem ante dapibus in viverra quis feugiat a tellus phasellus viverra nulla ut metus varius laoreet quisque rutrum.</p>
  <div class="more">READ MORE →</div><div class="count">💬 2</div>
</article>

<article class="abs card left" style="left:102px;top:581px">
  <div class="photo" role="img" aria-label="Grey room with pendant lamps, armchair and wall clock" style="background:linear-gradient(180deg,#7d8791,#a3acb4 55%,#4a4440)"></div>
  <div class="pointer"></div>
  <h2>Blog heading here</h2>
  <div class="meta"><i>By:</i> Admin &nbsp;&nbsp; <i>Date:</i> September 19th, 2016 &nbsp;&nbsp; <i>Tags:</i> Tag1, Tag2</div>
  <div class="rule"></div>
  <p>Aenean vulputate eleifend tellus aenean leo ligula porttitor eu consequat vitae eleifend ac enim aliquam lorem ante dapibus in viverra quis feugiat a tellus phasellus viverra nulla ut metus varius laoreet quisque rutrum.</p>
  <div class="more">READ MORE →</div><div class="count">💬 2</div>
</article>

<article class="abs card right" style="left:498px;top:581px">
  <div class="photo" role="img" aria-label="Red lounge chair beside a glowing cube lamp" style="background:linear-gradient(180deg,#b9ab92,#8d7c64 60%,#6b4a2a)"></div>
  <div class="pointer"></div>
  <h2>Blog heading here</h2>
  <div class="meta"><i>By:</i> Admin &nbsp;&nbsp; <i>Date:</i> September 19th, 2016 &nbsp;&nbsp; <i>Tags:</i> Tag1, Tag2</div>
  <div class="rule"></div>
  <p>Aenean vulputate eleifend tellus aenean leo ligula porttitor eu consequat vitae eleifend ac enim aliquam lorem ante dapibus in viverra quis feugiat a tellus phasellus viverra nulla ut metus varius laoreet quisque rutrum.</p>
  <div class="more">READ MORE →</div><div class="count">💬 2</div>
</article>

<div class="abs pager">
  <span class="wide">‹ PREV</span><span>1</span><span>....</span><span>3</span><span>4</span><span class="cur">5</span><span>6</span><span>7</span><span>....</span><span>94</span><span class="wide">NEXT ›</span>
</div>

<footer class="abs footer">
  <div class="fcol" style="left:63px;width:155px">
    <h3>About</h3>
    <p style="text-align:justify">The LUMOLUMO welcomes you to bright electronic space. Thousands of lights constantly growing and updated selected to illuminate your space at the best prices.</p>
    <div class="social"><span></span><span></span></div>
  </div>
  <div class="fcol" style="left:262px"><h3>Lumo Lumo</h3>
    <ul><li>The company</li><li>The shop</li><li>Cooperating companies</li><li>Data protection</li><li>Terms of use</li></ul></div>
  <div class="fcol" style="left:394px"><h3>Services</h3>
    <ul><li>Connection</li><li>record</li><li>Wish List</li><li>Basket</li><li>Communication</li></ul></div>
  <div class="fcol" style="left:495px"><h3>Information</h3>
    <ul><li>Payment methods</li><li>Shipping methods</li><li>Return policy</li><li>Returns form</li></ul></div>
  <div class="fcol" style="left:608px;width:180px"><h3>Newsletter</h3>
    <p>Subscribe to our newsletter to LUMOLINE first for our special offers!</p>
    <div class="email">Email Address</div>
    <div class="subscribe">Subscribe</div>
  </div>
</footer>

<div class="abs fbottom">
  <div class="copy">© Lumo Lumo, All Rights Reserved.</div>
  <div class="legal">Privacy Policy &nbsp;&nbsp; | &nbsp;&nbsp; Terms &amp; Conditions</div>
</div>
<div class="abs to-top">
  <svg width="28" height="28" viewBox="0 0 28 28" fill="none" stroke="#fff" stroke-width="1.2"><path d="M11.5 15.5 14 13l2.5 2.5"/></svg>
</div>

</body>
</html>
```